Mortgage Company Website / based from Moreno design

Mortgage company needs a WordPress site designed and developed using Pixel Harbor's Moreno framework. Existing site is BrellaMortgage.example.

Goals of website:
1) Attract new leads for Home loans (first-time home buyers, people moving to Dallas, and people re-financing their homes.
2) Attract and recruit new Loan Officers.

LOAN PRODUCTS OFFERED
Conventional
Jumbo
VA
FHA
USDA
Refinance
Construction Loans - not a main product. Don't like to do these.
Remodel

Target Market(s)

Middle to upper income families in the Dallas area.

Industry/Entity Type

Mortgage Brokerage

Coding

Coded - Design and coding required

Number of Pages Required

2 page

Requirements
Must have
• Must use one of the Moreno theme from Pixel Harbor for development
https://moreno.pixelharbor.example/

Client is focused on higher-end clientele and likes the use of the color gold.

NAVIGATION
Home Loans
Mortgage Resources
About Us
Contact Us

Site must also look good on mobile phones and tablets. Moreno theme has breakpoints already developed so should make that easier.
Nice to have
• Client likes the designs of these sites:
https://quenby.example/home-loans (this one was talked about as her favorite)
https://thewardlowpartners.example/
https://www.harborlinelending.example/

- Overall wants the site to be clean with lots of white space

Wants to keep the imagery focused on the families and people buying the home.

Also likes the focus on giving back to the community from the example site provided. Brella gives to "Hands for Tails"

Things that can be featured on the home page:
* Hero image on top
* Top of Z, Veltrix Market Leader award. Veltrix 100 Mortgage Market Leader 2020
* 3 Most recent blog posts
* Video from current homepage
* Get started form: Name, Email, Phone. Submit button
* Footer area can have navigation, contact info, and awards sections

some possible Moreno templates to choose from:
https://moreno.pixelharbor.example/charity/
https://moreno.pixelharbor.example/cryptocurrency/
https://moreno.pixelharbor.example/freelancer/
https://moreno.pixelharbor.example/finance/
https://moreno.pixelharbor.example/financial-advisor/
https://moreno.pixelharbor.example/university/
https://moreno.pixelharbor.example/marketing-consultant/

```html
<!DOCTYPE html>
<html lang="en">
<head>
<meta charset="utf-8">
<title>Brella Mortgage – Easy Home Loan &amp; Refinance</title>
<link href="https://fonts.googleapis.com/css2?family=Rubik:wght@400;500;700&family=Montserrat:wght@400;500;600&display=swap" rel="stylesheet">
<style>
:root{
  --gold:#cbb841;
  --gold-soft:#d9cb70;
  --ink:#232122;
  --dark:#2e2b2c;
  --black:#141414;
  --grey-bg:#efefef;
  --text:#444;
  --navy:#1b2d6b;
  --white:#fff;
}
*{margin:0;padding:0;box-sizing:border-box}
html,body{width:1200px;height:4751px;overflow:hidden}
body{position:relative;background:var(--white);font-family:"Montserrat",sans-serif;color:var(--text)}
.abs{position:absolute}
h1,h2,h3,.heading{font-family:"Rubik",sans-serif}

/* top bar + nav */
.topbar{left:0;top:0;width:1200px;height:40px;background:var(--black);color:#fff;font-size:14px}
.topbar .notice{position:absolute;left:262px;top:11px}
.topbar .notice a{color:#fff;text-decoration:underline;font-weight:600}
.topbar .phone{position:absolute;right:60px;top:10px;display:flex;gap:8px;align-items:center;font-size:16px}
.brand-box{left:46px;top:0;width:194px;height:115px;background:#fff;display:flex;flex-direction:column;align-items:center;justify-content:center}
.brand-name{font-family:"Rubik",sans-serif;font-weight:700;font-size:46px;color:var(--ink);line-height:1}
.brand-sub{font-size:9px;letter-spacing:4px;color:var(--ink);margin-top:6px}
.nav{left:0;top:40px;width:1200px;height:75px;background:#fff}
.nav ul{list-style:none;display:flex;gap:42px;position:absolute;left:375px;top:29px;font-size:14px;font-weight:600;color:var(--ink)}
.nav li.active{color:var(--gold)}
.apply{right:0;top:40px;width:201px;height:75px;background:var(--gold);color:#fff;padding:16px 0 0 33px}
.apply small{display:block;font-size:12px;font-weight:600}
.apply b{font-size:20px;font-weight:600}

/* hero */
.hero{left:0;top:115px;width:1200px;height:730px;background:linear-gradient(90deg,#cbbd57 0%,#d8ca78 35%,#b39a6c 60%,#ccc7bd 100%)}
.hero-copy{left:131px;top:300px;color:#fff}
.hero-copy h1{font-size:58px;font-weight:700;line-height:1.12}
.hero-copy h1 span{font-weight:500;font-size:48px}
.hero-copy p{font-size:20px;margin-top:16px}
.btn-dark{display:inline-flex;align-items:center;gap:12px;background:var(--ink);color:#fff;border-radius:30px;padding:13px 22px 13px 32px;font-weight:700;font-size:18px;margin-top:32px;font-family:"Rubik",sans-serif}
.circle-arrow{width:24px;height:24px;border-radius:50%;border:2px solid currentColor;display:inline-flex;align-items:center;justify-content:center}

/* welcome */
.welcome-img{left:120px;top:895px;width:433px;height:360px;border-radius:58% 42% 55% 45%/48% 55% 45% 52%;background:linear-gradient(135deg,#a48b74,#d9c2a8 55%,#7e6a5a);box-shadow:8px 10px 0 var(--gold)}
.welcome-swoosh{left:230px;top:885px;width:300px;height:60px}
.welcome-text{left:627px;top:918px;width:440px}
.eyebrow{font-family:"Rubik",sans-serif;font-size:26px;color:var(--ink)}
.welcome-text h2{font-size:42px;font-weight:700;color:var(--ink);line-height:1.1;white-space:nowrap}
.welcome-text p{font-size:14px;line-height:1.75;margin-top:22px;color:#333;width:420px}
.btn-outline{display:inline-flex;align-items:center;gap:12px;border:2px solid var(--gold);border-radius:24px;padding:8px 16px 8px 30px;font-size:14px;font-weight:600;color:var(--ink);margin-top:26px}
.btn-outline .circle-arrow{color:var(--gold);width:22px;height:22px}

/* services */
.services-head{left:0;top:1350px;width:1200px;text-align:center;color:var(--ink)}
.services-head .eyebrow{font-size:26px}
.services-head h2{font-size:40px;font-weight:700;margin-top:4px}
.band{left:0;top:1470px;width:1200px;height:840px}
.product{width:258px;height:258px;border-radius:50%;border:14px solid var(--dark);background:#fff;padding:6px}
.product.featured{border-color:var(--gold);width:282px;height:282px}
.product .photo{width:100%;height:100%;border-radius:50%;display:flex;flex-direction:column;align-items:center;justify-content:flex-end;padding-bottom:30px;color:#fff;font-family:"Rubik",sans-serif;font-size:20px;font-weight:500;gap:10px}
.product .circle-arrow{width:28px;height:28px}
.product.featured .circle-arrow{color:var(--gold)}
.slide-arrow{width:36px;height:36px;border-radius:50%;display:flex;align-items:center;justify-content:center}

/* what we do */
.video-card{left:0;top:1870px;width:572px;height:440px}
.wwd{left:649px;top:1905px;width:430px;color:#fff}
.wwd h2{font-size:42px;font-weight:700}
.wwd p{font-size:16px;line-height:1.5;margin-top:26px}
.wwd .btn-outline{color:#fff;padding:8px 38px;font-size:16px;margin-top:28px}

/* awards */
.awards{left:0;top:2307px;width:1200px;height:610px;background:var(--grey-bg)}
.awards h2{position:absolute;top:64px;width:100%;text-align:center;font-size:40px;font-weight:700;color:var(--ink)}
.award{top:140px;width:270px;height:358px;border:6px solid #8d8d8d;background:#fff}
.award .photo{width:100%;height:100%}
.dots{top:530px;left:565px;display:flex;gap:8px}
.dots span{width:14px;height:14px;border-radius:50%;border:2px solid #aaa;background:#d8d8d8}
.dots span.on{background:var(--gold);border-color:var(--gold);width:18px;height:18px;margin-top:-2px}

/* blog */
.blog-head{left:0;top:2970px;width:1200px;text-align:center;font-size:42px;font-weight:700;color:var(--ink)}
.post{top:3059px;width:303px}
.post .photo{height:175px}
.post h3{font-size:19px;font-weight:500;color:var(--ink);line-height:1.3;margin-top:34px}
.post p{font-size:13px;line-height:1.6;color:#555;margin-top:8px}
.post .btn-outline{font-size:12px;padding:6px 12px 6px 24px;margin-top:22px}

/* estimate */
.estimate-head{left:0;top:3515px;width:1200px;text-align:center;font-size:38px;font-weight:700;color:var(--ink)}
.estimate-head span{color:var(--navy)}
.lifestyle{left:0;top:3833px;width:1200px;height:590px;background:linear-gradient(90deg,#d7c86a,#e2d68f 45%,#c7b54e 75%,#b09d52)}
.form-card{left:295px;top:3631px;width:612px;height:424px;background:#fff;box-shadow:0 4px 18px rgba(0,0,0,.15)}
.field{position:absolute;border:2px solid #ccc;font-size:13px;color:#333;padding:8px 0 0 40px;height:36px}
.field.area{height:110px;padding-top:14px}
.select-caret{position:absolute;right:0;top:0;width:44px;height:100%;background:#333;display:flex;align-items:center;justify-content:center}
.btn-gold{position:absolute;background:var(--gold);color:#fff;font-size:15px;font-weight:600;display:flex;align-items:center;justify-content:center;gap:10px}
.dot-arrow{width:16px;height:16px;border-radius:50%;background:#fff;display:inline-flex;align-items:center;justify-content:center}
.about-you{left:0;top:4105px;width:1200px;text-align:center;color:var(--ink)}
.about-you h3{font-size:26px;font-weight:700}
.about-you p{font-size:17px;line-height:1.45;margin-top:8px}
.btn-ink{display:inline-flex;align-items:center;gap:10px;background:var(--ink);color:#fff;font-size:15px;padding:12px 28px;margin-top:32px}

/* footer */
.footer{left:0;top:4423px;width:1200px;height:328px;background:var(--ink);color:#fff}
.footer .brand-name{color:#fff;font-size:44px}
.footer-brand{left:150px;top:52px;display:flex;flex-direction:column;align-items:center}
.footer-brand .brand-sub{color:#fff}
.footer ul{list-style:none;position:absolute;font-size:13px;font-weight:600;line-height:2.2}
.footer ul.links li{text-decoration:underline;font-weight:500}
.map{left:787px;top:44px;width:280px;height:111px;background:linear-gradient(135deg,#dfe6ee,#c9d3de 50%,#e8ecef)}
.social{left:525px;top:205px;display:flex;gap:8px}
.social span{width:30px;height:30px;border:2px solid #fff;border-radius:50%}
.copy{left:0;top:254px;width:1200px;border-top:1px solid #444;padding-top:26px;text-align:center;font-size:13px;color:#ddd}
</style>
</head>
<body>

<div class="abs topbar">
  <div class="notice">For information on our response to COVID-19 <a>Click Here</a></div>
  <div class="phone">
    <svg width="16" height="16" viewBox="0 0 24 24"><path fill="#fff" d="M6.6 10.8a15.1 15.1 0 0 0 6.6 6.6l2.2-2.2c.3-.3.7-.4 1-.2 1.1.4 2.3.6 3.6.6.6 0 1 .4 1 1V20c0 .6-.4 1-1 1A17 17 0 0 1 3 4c0-.6.4-1 1-1h3.5c.6 0 1 .4 1 1 0 1.3.2 2.5.6 3.6.1.3 0 .7-.2 1z"/></svg>
    555-014-0363
  </div>
</div>
<div class="abs nav">
  <ul><li class="active">HOME LOANS</li><li>MORTGAGE RESOURCES</li><li>ABOUT US</li><li>CONTACT US</li></ul>
</div>
<div class="abs brand-box"><span class="brand-name">Brella</span><span class="brand-sub">MORTGAGE INC</span></div>
<div class="abs apply"><small>FREE ESTIMATES</small><b>APPLY NOW</b></div>

<!-- hero -->
<div class="abs hero" role="img" aria-label="Family sitting on a living room floor holding a cardboard roof over their heads, gold-tinted interior"></div>
<svg class="abs" style="left:0;top:730px" width="1200" height="120" viewBox="0 0 1200 120">
  <polygon points="0,120 0,100 690,18 1200,103 1200,120" fill="#fff"/>
  <polyline points="690,18 1200,103" stroke="var(--gold)" stroke-width="3" fill="none"/>
</svg>
<div class="abs hero-copy">
  <h1>Easy Home<br>Loan <span>&amp; Refinance</span></h1>
  <p>Get Your Rate In Minutes</p>
  <div class="btn-dark">GET STARTED <span class="circle-arrow"><svg width="12" height="12" viewBox="0 0 12 12"><path d="M2 8l4-4 4 4" stroke="#fff" stroke-width="2" fill="none"/></svg></span></div>
</div>

<!-- welcome -->
<svg class="abs welcome-swoosh" viewBox="0 0 300 60"><path d="M0 50C60 10 140 0 210 25s70 25 90 35" stroke="var(--gold)" stroke-width="14" fill="none" stroke-linecap="round"/></svg>
<div class="abs welcome-img" role="img" aria-label="Smiling couple signing papers beside a small model house"></div>
<div class="abs welcome-text">
  <div class="eyebrow">WELCOME TO</div>
  <h2>BRELLA MORTGAGE</h2>
  <p>Brella Mortgage is founded with passion and the heart of serving. We strive to keep the mortgage experience simple, efficient, and enjoyable for our clients. Brella Mortgage is here to serve you whether you are looking for the best rates in town with a quick.</p>
  <div class="btn-outline">LEARN MORE <span class="circle-arrow"><svg width="10" height="10" viewBox="0 0 12 12"><path d="M2 8l4-4 4 4" stroke="var(--gold)" stroke-width="2" fill="none"/></svg></span></div>
</div>
<div class="abs" style="left:1030px;top:1140px;width:170px;height:420px;background:linear-gradient(180deg,rgba(235,235,235,0),rgba(235,235,235,.6))" role="img" aria-label="Faint line illustration of tall buildings"></div>

<!-- services -->
<div class="abs" style="left:0;top:1470px;width:330px;height:200px;background:linear-gradient(180deg,rgba(235,235,235,.6),rgba(235,235,235,0))" role="img" aria-label="Faint line illustration of a house"></div>
<div class="abs services-head">
  <div class="eyebrow">SCREVICES</div>
  <h2>LOAN PRODUCTS OFFERED</h2>
</div>
<svg class="abs band" viewBox="0 0 1200 840" aria-hidden="true">
  <polygon points="0,310 470,150 1200,95 1200,140 470,190 0,345" fill="var(--gold)"/>
  <polygon points="0,345 470,190 1200,140 1200,840 0,840" fill="var(--dark)"/>
</svg>
<div class="abs" style="left:0;top:1790px;width:1200px;height:517px;background:linear-gradient(180deg,rgba(46,43,44,0),rgba(70,64,60,.6) 40%,rgba(46,43,44,.9))" role="img" aria-label="Faint background photo of a family reading together"></div>

<div class="abs slide-arrow" style="left:140px;top:1613px;background:var(--dark)"><svg width="14" height="14" viewBox="0 0 14 14"><path d="M9 2L4 7l5 5" stroke="#fff" stroke-width="2.4" fill="none"/></svg></div>
<div class="abs slide-arrow" style="left:1023px;top:1613px;background:#fff"><svg width="14" height="14" viewBox="0 0 14 14"><path d="M5 2l5 5-5 5" stroke="var(--dark)" stroke-width="2.4" fill="none"/></svg></div>

<div class="abs product" style="left:212px;top:1497px">
  <div class="photo" role="img" aria-label="Couple reviewing loan papers with a model house" style="background:linear-gradient(160deg,#c9c1b6,#8a7e72)">Conventional<span class="circle-arrow"><svg width="12" height="12" viewBox="0 0 12 12"><path d="M2 8l4-4 4 4" stroke="#fff" stroke-width="2" fill="none"/></svg></span></div>
</div>
<div class="abs product featured" style="left:454px;top:1485px">
  <div class="photo" role="img" aria-label="Hand holding house keys over stacked coins" style="background:linear-gradient(160deg,#d89a4c,#8a4e22)">Jumbo<span class="circle-arrow"><svg width="12" height="12" viewBox="0 0 12 12"><path d="M2 8l4-4 4 4" stroke="var(--gold)" stroke-width="2" fill="none"/></svg></span></div>
</div>
<div class="abs product" style="left:728px;top:1497px">
  <div class="photo" role="img" aria-label="Agent handing keys to a smiling homeowner" style="background:linear-gradient(160deg,#b59a86,#5f4a3e)">Refinance<span class="circle-arrow"><svg width="12" height="12" viewBox="0 0 12 12"><path d="M2 8l4-4 4 4" stroke="#fff" stroke-width="2" fill="none"/></svg></span></div>
</div>

<!-- what we do -->
<svg class="abs video-card" viewBox="0 0 572 440" aria-hidden="true">
  <path d="M0 150C80 90 200 10 330 2c120-8 220 40 232 170 10 110-40 200-110 268H0z" fill="var(--gold)"/>
  <path d="M0 150C80 95 200 20 325 14c110-6 210 40 220 160 8 105-42 195-108 266H0z" fill="#fff"/>
</svg>
<div class="abs" style="left:40px;top:1920px;width:480px;height:387px;background:linear-gradient(180deg,rgba(255,255,255,0),rgba(200,200,200,.35))" role="img" aria-label="Video preview showing the company name, phone number and web address"></div>
<div class="abs" style="left:300px;top:2062px;width:74px;height:74px;border-radius:50%;background:rgba(20,20,20,.85);display:flex;align-items:center;justify-content:center">
  <svg width="26" height="28" viewBox="0 0 26 28"><path d="M4 2l20 12L4 26z" fill="#fff"/></svg>
</div>
<div class="abs wwd">
  <h2>WHT WE DO?</h2>
  <p>Lorem Ipsum is simply dummy text of the printing and typesetting industry. Lorem Ipsum has been the industry's standard dummy text ever since the 1500s, when an unknown printer took a galley of type and scrambled it to make.</p>
  <div class="btn-outline">Learn More</div>
</div>

<!-- awards -->
<div class="abs awards">
  <h2>AWARDS</h2>
  <div class="abs award" style="left:160px"><div class="photo" role="img" aria-label="Magazine cover for the Veltrix 2020 market leader issue" style="background:linear-gradient(180deg,#3a3a3a 0%,#6a6a6a 45%,#efe9df 46%,#d8d0c4 100%)"></div></div>
  <div class="abs award" style="left:459px"><div class="photo" role="img" aria-label="Magazine page listing the 2020 market leader top 100" style="background:linear-gradient(180deg,#e6e2dc,#cfc9c0)"></div></div>
  <div class="abs award" style="left:755px"><div class="photo" role="img" aria-label="Veltrix market leaders feature page with a photo of a house" style="background:linear-gradient(180deg,#f1eee9 0%,#e4ded4 45%,#8a8580 46%,#6f6a66 70%,#ebe7e1 71%)"></div></div>
  <div class="abs dots"><span></span><span class="on"></span><span></span></div>
</div>

<!-- blog -->
<h2 class="abs blog-head">RECENT BLOG</h2>
<div class="abs post" style="left:131px">
  <div class="photo" role="img" aria-label="Homeowner receiving house keys" style="background:linear-gradient(135deg,#7d6a5d,#c8b8a6)"></div>
  <h3>Lorem Ipsum is simply dummy text of the the industry's</h3>
  <p>Lorem Ipsum is simply dummy text of the printing and typesetting industry. Lorem Ipsum has industry's standard...</p>
  <div class="btn-outline">LEARN MORE <span class="circle-arrow"><svg width="10" height="10" viewBox="0 0 12 12"><path d="M2 8l4-4 4 4" stroke="var(--gold)" stroke-width="2" fill="none"/></svg></span></div>
</div>
<div class="abs post" style="left:449px">
  <div class="photo" role="img" aria-label="Model house on a desk with documents" style="background:linear-gradient(135deg,#9e9a96,#e7e4df)"></div>
  <h3>Lorem Ipsum is simply dummy text of the the industry's</h3>
  <p>Lorem Ipsum is simply dummy text of the printing and typesetting industry. Lorem Ipsum has industry's standard...</p>
  <div class="btn-outline">LEARN MORE <span class="circle-arrow"><svg width="10" height="10" viewBox="0 0 12 12"><path d="M2 8l4-4 4 4" stroke="var(--gold)" stroke-width="2" fill="none"/></svg></span></div>
</div>
<div class="abs post" style="left:765px">
  <div class="photo" role="img" aria-label="Handshake across a desk beside a small model house" style="background:linear-gradient(135deg,#3d4450,#b6b8bd)"></div>
  <h3>Lorem Ipsum is simply dummy text of the the industry's</h3>
  <p>Lorem Ipsum is simply dummy text of the printing and typesetting industry. Lorem Ipsum has industry's standard...</p>
  <div class="btn-outline">LEARN MORE <span class="circle-arrow"><svg width="10" height="10" viewBox="0 0 12 12"><path d="M2 8l4-4 4 4" stroke="var(--gold)" stroke-width="2" fill="none"/></svg></span></div>
</div>

<!-- estimate -->
<h2 class="abs estimate-head">GET A &nbsp;<span>FREE ESTIMATE</span></h2>
<div class="abs lifestyle" role="img" aria-label="Gold-tinted photo of a smiling family relaxing on a sofa"></div>
<div class="abs form-card">
  <div class="field" style="left:51px;top:36px;width:244px">NAME</div>
  <div class="field" style="left:313px;top:36px;width:244px;padding-left:12px">PHONE</div>
  <div class="field" style="left:51px;top:90px;width:244px">EMAIL</div>
  <div class="field" style="left:313px;top:90px;width:244px;padding-left:12px">ADDRESS</div>
  <div class="field" style="left:51px;top:145px;width:506px">ESTIMATE TYPE<span class="select-caret"><svg width="14" height="8" viewBox="0 0 14 8"><path d="M0 0h14L7 8z" fill="#fff"/></svg></span></div>
  <div class="field area" style="left:51px;top:199px;width:506px">HOW CAN WE HELP ?</div>
  <div class="btn-gold" style="left:315px;top:326px;width:242px;height:44px">START MY ESTIMATE <span class="dot-arrow"><svg width="8" height="8" viewBox="0 0 8 8"><path d="M2 1l4 3-4 3" stroke="var(--gold)" stroke-width="1.6" fill="none"/></svg></span></div>
</div>
<div class="abs about-you">
  <h3>It's all about you!</h3>
  <p>We are reinventing the mortgage infastructure by<br>putting you at the center!</p>
  <div class="btn-ink">START MY ESTIMATE <span class="dot-arrow" style="background:var(--gold)"><svg width="8" height="8" viewBox="0 0 8 8"><path d="M2 1l4 3-4 3" stroke="#fff" stroke-width="1.6" fill="none"/></svg></span></div>
</div>

<!-- footer -->
<footer class="abs footer">
  <div class="abs footer-brand"><span class="brand-name">Brella</span><span class="brand-sub">MORTGAGE INC</span></div>
  <ul style="left:365px;top:38px"><li>HOME LOANS</li><li>MORTGAGE RESOURCES</li><li>ABOUT US</li><li>CONTACT US</li></ul>
  <ul style="left:617px;top:36px"><li>ABOUT US</li></ul>
  <ul class="links" style="left:617px;top:66px;line-height:2.1"><li>FAQ</li><li>Testimonials</li><li>Sitemap</li></ul>
  <div class="abs map" role="img" aria-label="Street map showing the office location"></div>
  <svg class="abs" style="left:917px;top:78px" width="18" height="24" viewBox="0 0 18 24"><path d="M9 0a9 9 0 0 0-9 9c0 7 9 15 9 15s9-8 9-15a9 9 0 0 0-9-9z" fill="#e0344a"/><circle cx="9" cy="9" r="3.5" fill="#fff"/></svg>
  <div class="abs social"><span></span><span></span><span></span><span></span></div>
  <div class="abs copy">© 2020 Brella Mortgage. All Rights are Reserved.</div>
</footer>

</body>
</html>
```